Torvel Business Cards

Business card design. dont mind if new logo is suggested.
it would be for a security company.
our clients would be bigger security companies around Australia.
have a logo done but can be replaced. see attaached. like the colors.
Need company name, person name, designation, phone and email on front.
At back company logo and name. website saddress and 2 x license numbers
would like to have 2 different background color for both sidde

Industry/Entity Type

Security

Contact Information for Business Card

round corners, front should be light in color. need logo at back with webaddress and 2 x license numners

Font styles to use
Sans Serif

Colors
f37122
faa54b
f8ba93
0255a3
0592cd
85cae6
b3d448
9bcb3c
ffffff

Requirements
Must have
• see description
Nice to have
• see description
Should not have
• should not be difficult to read or hardd to find information on card.. lets say easy on eyes yet catchy

```html
<!DOCTYPE html>
<html lang="en">
<head>
<meta charset="utf-8">
<title>Torvel Security Group – Business Cards</title>
<link rel="stylesheet" href="https://fonts.googleapis.com/css2?family=Arimo:wght@400;700&family=Tinos:wght@400&display=swap">
<style>
  :root {
    --stage: #3a2a36;
    --card-light: #ffffff;
    --card-dark: #0b0b0c;
    --ink-blue: #0255a3;
    --bright-blue: #0592cd;
    --sky-blue: #85cae6;
    --band-black: #0a0a0a;
    --band-grey: #b9b9b9;
    --white: #ffffff;
  }
  * { box-sizing: border-box; margin: 0; padding: 0; }
  html, body { width: 1200px; height: 800px; overflow: hidden; }
  body {
    background: radial-gradient(ellipse at 50% 45%, #6a3a34 0%, var(--stage) 60%, #241e33 100%);
    position: relative;
    font-family: "Arimo", Arial, sans-serif;
  }
  .card {
    position: absolute;
    top: 250px;
    width: 510px;
    height: 300px;
    border-radius: 18px;
    overflow: hidden;
    box-shadow: 0 14px 30px rgba(0,0,0,0.45);
  }

  /* Back of card */
  .card-back {
    left: 50px;
    background: linear-gradient(160deg, #1d1d1f 0%, var(--card-dark) 70%);
  }
  .back-brand {
    position: absolute;
    left: 0; right: 0; top: 92px;
    display: flex; align-items: center; justify-content: center; gap: 14px;
  }
  .brand-dot {
    width: 30px; height: 30px; border-radius: 50%;
    background: var(--bright-blue);
  }
  .brand-name {
    font-family: "Tinos", "Times New Roman", serif;
    font-size: 34px;
    letter-spacing: 1px;
    color: var(--ink-blue);
    font-weight: 400;
  }
  .back-licence {
    position: absolute; left: 0; right: 0; top: 160px;
    text-align: center;
    font-size: 13px; color: var(--ink-blue);
  }
  .back-licence span + span { margin-left: 12px; }
  .back-web {
    position: absolute; left: 0; right: 0; top: 222px;
    text-align: center;
    font-size: 15px; color: var(--ink-blue);
  }

  /* Front of card */
  .card-front {
    left: 640px;
    background: var(--card-light);
  }
  .front-company {
    position: absolute; left: 176px; top: 30px;
    font-size: 12px; letter-spacing: 0.5px; color: var(--bright-blue);
  }
  .front-bubbles {
    position: absolute; right: 0; top: 40px;
    width: 300px; height: 260px;
    background: radial-gradient(ellipse at 65% 55%, rgba(133,202,230,0.55) 0%, rgba(133,202,230,0.25) 45%, rgba(255,255,255,0) 75%);
  }
  .name-band {
    position: absolute; left: 0; top: 52px;
    width: 390px; height: 88px;
    background: var(--band-black);
    border-top: 3px double var(--band-grey);
    border-bottom: 3px double var(--band-grey);
    border-right: 3px double var(--band-grey);
  }
  .person-name {
    position: absolute; left: 26px; top: 12px;
    font-size: 44px; font-weight: 700; color: var(--white);
  }
  .person-role {
    position: absolute; left: 28px; top: 60px;
    font-size: 17px; color: var(--band-grey);
  }
  .front-contact {
    position: absolute; left: 28px; top: 162px;
    font-size: 17px; line-height: 26px; color: var(--ink-blue);
  }
</style>
</head>
<body>
  <section class="card card-back" aria-label="Card back">
    <div class="back-brand">
      <span class="brand-dot"></span>
      <span class="brand-name">TORVEL SECURITY GROUP</span>
    </div>
    <p class="back-licence"><span>ACT Government 17509914</span><span>ABN 58203917460</span></p>
    <p class="back-web">www.northgateworks.com.au</p>
  </section>

  <section class="card card-front" aria-label="Card front">
    <div class="front-bubbles" role="img" aria-label="Soft pale blue bubble pattern"></div>
    <p class="front-company">TORVEL SECURITY GROUP</p>
    <div class="name-band">
      <p class="person-name">Alex Reed</p>
      <p class="person-role">Director</p>
    </div>
    <div class="front-contact">
      <p class="contact-email">alex@torvelsecurity.com.au</p>
      <p class="contact-phone">0412 708 351</p>
    </div>
  </section>
</body>
</html>
```